The book is titled "DREAM BUILD SOAR with a VICTOR"
It is written by a psychologist who is a former world champion, Australian captain and qualified organizational psychologist.
I have added the components of my champion star.
The book should reflect the qualities of champions..
BOLD COLOURFUL

Target Market(s)

16 to 60 year athletes coaches and club administrators (from average to elite). Much of the book also crosses to being a champion in other fields

Requirements
Must have
• The title
Smaller font An expert guide with practical solutions
The star some where
The top of field momentum logo ( can be small in corner)
My name as R T Hollins (M Psych, World Champion)
Bold Font biggest for Champion (to be a...smaller)

Can you please add
Player Team Coach Leader CEO

Like my name at the bottom

Colourful (can be fluoro)
Need A5 (main book) and A4 options for some schools who photocopy.
Nice to have
• Spine the book is 250 pages
Back design.. just colours or you can put the star there

```html
<!DOCTYPE html>
<html lang="en">
<head>
<meta charset="utf-8">
<title>Dream Build Soar with a Victor — Book Cover</title>
<link rel="stylesheet" href="https://fonts.googleapis.com/css2?family=Anton&family=Archivo+Black&family=Tinos:ital@0;1&display=swap">
<style>
  :root {
    --page: #ffffff;
    --leather-deep: #020202;
    --leather-mid: #121212;
    --spine-line: #3a3a3a;
    --blue: #1530d8;
    --orange: #e2470c;
    --yellow: #f4ec0a;
    --red-italic: #7a0c0c;
    --green: #5cc21e;
    --name-yellow: #f2ea2a;
    --logo-blue: #27a3e6;
  }
  html, body {
    margin: 0;
    padding: 0;
    width: 1200px;
    height: 1000px;
    overflow: hidden;
    background: var(--page);
  }
  .canvas {
    position: relative;
    width: 1200px;
    height: 1000px;
    background: var(--page);
  }
  .cover-wrap {
    position: absolute;
    left: 0;
    top: 83px;
    width: 1200px;
    height: 820px;
    background:
      radial-gradient(ellipse at 70% 30%, #1a1a1a 0%, transparent 60%),
      radial-gradient(ellipse at 25% 60%, #141414 0%, transparent 55%),
      linear-gradient(180deg, var(--leather-mid), var(--leather-deep));
    overflow: hidden;
  }
  .spine {
    position: absolute;
    left: 577px;
    top: 0;
    width: 46px;
    height: 820px;
    border-left: 2px solid var(--spine-line);
    border-right: 2px solid var(--spine-line);
    box-sizing: border-box;
  }
  .spine-title {
    position: absolute;
    left: 621px;
    top: 27px;
    transform-origin: 0 0;
    transform: rotate(90deg);
    white-space: nowrap;
    font-family: "Anton", sans-serif;
    font-size: 36px;
    line-height: 40px;
    letter-spacing: 0.5px;
  }
  .spine-title .small {
    font-family: "Tinos", serif;
    font-style: italic;
    font-size: 15px;
    color: var(--red-italic);
    padding: 0 3px;
  }
  .spine-author {
    position: absolute;
    left: 613px;
    top: 657px;
    transform-origin: 0 0;
    transform: rotate(90deg);
    white-space: nowrap;
    font-family: "Tinos", serif;
    font-size: 21px;
    line-height: 26px;
    color: var(--name-yellow);
  }
  .c-blue { color: var(--blue); }
  .c-orange { color: var(--orange); }
  .c-yellow { color: var(--yellow); }
  .c-green { color: var(--green); }

  .front-title {
    position: absolute;
    left: 690px;
    top: 0;
    width: 455px;
    height: 560px;
    text-align: center;
    font-family: "Anton", sans-serif;
    text-transform: uppercase;
    margin: 0;
    font-weight: 400;
  }
  .title-line {
    position: absolute;
    left: 0;
    width: 100%;
    display: block;
    font-size: 90px;
    line-height: 90px;
    letter-spacing: 2px;
    transform: scaleX(1.08);
    text-shadow: 3px 3px 4px rgba(0,0,0,0.9);
  }
  .line-1 { top: 137px; }
  .line-2 { top: 227px; }
  .line-3 { top: 320px; }
  .line-connector {
    position: absolute;
    left: 0;
    top: 400px;
    width: 100%;
    z-index: 2;
    font-family: "Tinos", serif;
    font-style: italic;
    font-size: 42px;
    line-height: 44px;
    text-transform: none;
    color: var(--red-italic);
  }
  .line-4 { top: 450px; font-size: 92px; line-height: 92px; transform: scaleX(1.12); }

  .subtitle {
    position: absolute;
    left: 920px;
    top: 553px;
    width: 222px;
    text-align: right;
    font-family: "Archivo Black", sans-serif;
    font-size: 19px;
    line-height: 24px;
    color: var(--yellow);
    margin: 0;
  }
  .star-emblem {
    position: absolute;
    left: 652px;
    top: 682px;
    width: 106px;
    height: 106px;
    border-radius: 50%;
    background: conic-gradient(from 0deg, #f29ab8, #8bd21c, #7a1fa8, #1a9ee0, #b427c8, #ef7d1a, #f29ab8);
    opacity: 0.85;
  }
  .author {
    position: absolute;
    left: 795px;
    top: 690px;
    margin: 0;
    font-family: "Tinos", serif;
    font-size: 36px;
    line-height: 40px;
    color: var(--name-yellow);
    font-weight: 400;
  }
  .credentials {
    position: absolute;
    left: 795px;
    top: 749px;
    margin: 0;
    font-family: "Tinos", serif;
    font-size: 19px;
    line-height: 22px;
    color: var(--name-yellow);
  }
  .publisher {
    position: absolute;
    left: 1070px;
    top: 700px;
    width: 100px;
    display: flex;
    flex-direction: column;
    align-items: center;
    gap: 6px;
  }
  .publisher-mark {
    width: 26px;
    height: 26px;
    border-radius: 50%;
    background: var(--logo-blue);
  }
  .publisher-name {
    font-family: "Archivo Black", sans-serif;
    font-size: 11px;
    line-height: 13px;
    text-align: center;
    color: var(--logo-blue);
  }
</style>
</head>
<body>
<div class="canvas">
  <div class="cover-wrap">
    <section class="back-cover" aria-label="Back cover"></section>

    <div class="spine" aria-hidden="true"></div>
    <div class="spine-title">
      <span class="c-blue">DREAM</span><span class="c-orange">BUILD</span><span class="c-yellow">SOAR</span><span class="small">with a</span><span class="c-green">VICTOR</span>
    </div>
    <div class="spine-author">R T Hollins</div>

    <section class="front-cover" aria-label="Front cover">
      <h1 class="front-title">
        <span class="title-line line-1 c-blue">Dream</span>
        <span class="title-line line-2 c-orange">Build</span>
        <span class="title-line line-3 c-yellow">Soar</span>
        <span class="line-connector">with a</span>
        <span class="title-line line-4 c-green">Victor</span>
      </h1>
      <p class="subtitle">An expert guide</p>

      <div class="star-emblem" role="img" aria-label="Multicoloured champion star emblem"></div>

      <p class="author">R T Hollins</p>
      <p class="credentials">M Psych, World Champion</p>

      <div class="publisher">
        <span class="publisher-mark" aria-hidden="true"></span>
        <span class="publisher-name">top of field momentum</span>
      </div>
    </section>
  </div>
</div>
</body>
</html>
```